Sign Design

We already have a logo, but would like to design 2 x signs.
Sign 1:
Dimensions 1500mm wide x 2500m high.
Information to include on sign: - Clinic name and logo (attached)
- the word "DENTIST "
- Street number (which is 348)
Phone number (which is 6153 4097)

Sign 2:
Dimensions: 800mm wide x 600mm high

```html
<!DOCTYPE html>
<html lang="en">
<head>
<meta charset="utf-8">
<title>Kellbrook Dental Care – Signage</title>
<link rel="stylesheet" href="https://fonts.googleapis.com/css2?family=Anton&family=Montserrat:wght@500;800;900&family=Oswald:wght@500&display=swap">
<style>
  :root {
    --backdrop: #312d2c;
    --white: #ffffff;
    --black: #000000;
    --brand-green: #1db24b;
    --brand-dark: #1a7a3c;
    --leaf-light: #dfe9b3;
    --leaf-mid: #a3cf4c;
    --photo-cool: #a7b7c8;
    --photo-warm: #ece6e1;
  }
  html, body {
    margin: 0;
    padding: 0;
    width: 667px;
    height: 1200px;
    overflow: hidden;
    background: var(--backdrop);
  }
  .artboard {
    position: relative;
    width: 667px;
    height: 1200px;
  }
  .sign {
    position: absolute;
    display: block;
  }
  .sign--landscape { left: 67px; top: 50px; width: 533px; height: 400px; }
  .sign--portrait  { left: 173px; top: 548px; width: 320px; height: 533px; }

  .brand-name { font-family: "Montserrat", sans-serif; font-weight: 500; fill: var(--brand-dark); }
  .headline-wide { font-family: "Montserrat", sans-serif; font-weight: 900; fill: var(--brand-green); }
  .headline-condensed { font-family: "Anton", sans-serif; fill: var(--white); }
  .address-wide { font-family: "Montserrat", sans-serif; font-weight: 800; fill: var(--black); }
  .address-condensed { font-family: "Oswald", sans-serif; font-weight: 500; fill: var(--black); }
  .phone { font-family: "Montserrat", sans-serif; font-weight: 900; fill: var(--black); }
</style>
</head>
<body>
<main class="artboard">

  <!-- Sign 2: 800 x 600 -->
  <svg class="sign sign--landscape" viewBox="0 0 1145 859" xmlns="http://www.w3.org/2000/svg" aria-label="Kellbrook Dental Care dentist sign, landscape">
    <defs><style>.bg-white{fill:var(--white)}.bg-green{fill:var(--brand-green)}.bg-black{fill:var(--black)}.bg-leaf{fill:var(--leaf-light)}.mark{fill:var(--leaf-mid)}</style></defs>
    <rect class="bg-white" x="0" y="0" width="1145" height="859"/>
    <path class="bg-green" d="M0 246 C 300 222, 560 268, 710 312 C 860 354, 1010 318, 1145 228 L1145 598 L0 598 Z"/>
    <path class="bg-black" d="M0 280 C 300 252, 560 292, 710 332 C 860 370, 1010 338, 1145 250 L1145 598 L0 598 Z"/>
    <rect class="bg-leaf" x="0" y="598" width="1145" height="261"/>
    <circle class="mark" cx="205" cy="170" r="105"/>
    <text class="brand-name" x="397" y="197" font-size="130" textLength="670" lengthAdjust="spacingAndGlyphs">Kellbrook</text>
    <text class="brand-name" x="630" y="278" font-size="72" textLength="387" lengthAdjust="spacingAndGlyphs">Dental Care</text>
    <text class="headline-wide" x="47" y="563" font-size="220" textLength="1045" lengthAdjust="spacingAndGlyphs">DENTIST</text>
    <text class="address-wide" x="185" y="665" font-size="68" textLength="770" lengthAdjust="spacingAndGlyphs">STREET NUMBER 348</text>
    <text class="phone" x="47" y="828" font-size="196" textLength="1035" lengthAdjust="spacingAndGlyphs">6153 4097</text>
  </svg>

  <!-- Sign 1: 1500 x 2500 -->
  <svg class="sign sign--portrait" viewBox="0 0 687 1144" xmlns="http://www.w3.org/2000/svg" aria-label="Kellbrook Dental Care dentist sign, portrait">
    <defs>
      <style>.bg-white{fill:var(--white)}.bg-green{fill:var(--brand-green)}.curve-line{fill:none;stroke:var(--brand-green);stroke-width:12}.mark{fill:var(--leaf-mid)}</style>
      <linearGradient id="photo-tone" x1="0" y1="0" x2="1" y2="1">
        <stop offset="0" stop-color="var(--photo-cool)"/>
        <stop offset="1" stop-color="var(--photo-warm)"/>
      </linearGradient>
    </defs>
    <rect class="bg-white" x="0" y="0" width="687" height="1144"/>
    <path role="img" aria-label="Photo: smiling patient in a dental chair during a check-up" fill="url(#photo-tone)"
          d="M0 178 C 40 250, 150 272, 300 257 C 450 238, 530 226, 600 240 C 650 252, 680 275, 687 295 L687 701 L0 701 Z"/>
    <path class="curve-line" d="M0 178 C 40 250, 150 272, 300 257 C 450 238, 530 226, 600 240 C 650 252, 680 275, 687 295"/>
    <path class="bg-green" d="M0 701 L687 701 L687 880 C 620 910, 520 925, 400 900 C 250 870, 120 880, 0 968 Z"/>
    <circle class="mark" cx="95" cy="110" r="70"/>
    <text class="brand-name" x="253" y="133" font-size="80" textLength="395" lengthAdjust="spacingAndGlyphs">Kellbrook</text>
    <text class="brand-name" x="390" y="178" font-size="42" textLength="230" lengthAdjust="spacingAndGlyphs">Dental Care</text>
    <text class="headline-condensed" x="53" y="868" font-size="172" textLength="585" lengthAdjust="spacingAndGlyphs">DENTIST</text>
    <text class="address-condensed" x="46" y="1003" font-size="76" textLength="594" lengthAdjust="spacingAndGlyphs">STREET NUMBER 348</text>
    <text class="phone" x="48" y="1103" font-size="112" textLength="590" lengthAdjust="spacingAndGlyphs">6153 4097</text>
  </svg>

</main>
</body>
</html>
```